Cover for "ROOTED! The skill and rhythm of guiding teams through calm and delight"

My first book for a global audience of modern performance leaders needs its cover!
I am an international executive coach and I've developed a new approach to replace classic Performance Management with a natural, sustainable approach fit for human beings :) My first book is about this approach and serves two purposes: helping leaders and sparking their curiosity to learn more, and positioning myself as a thought leader in the field.
The book is built on personal experience; it is both professional and personal ("From me to You"), and I'd like to position it beyond classic categorisation.
Its cover should communicate humanness, naturalness, ease and joy, within an unmistakably business-y context. I would like to see designs that use the color yellow (but not sure it communicates the right things).
Updates

Target Market(s)

Leaders who aspire to have a positive impact and deliver results in a meaningful way

Industry/Entity Type

Consulting & Executive Coaching - Trusted Advisor

Font styles to use
Other font styles liked:
• Helvetica Neue

Colors
0094D4
00A9DD
6FCCEA
C7EBF8
E9F6FB
FFC000
F8CF3A
FAE287
FDF2CF
FEFAEE
EE7325
F08F49
F5BC92
FAE3D3
FDF4ED

Requirements
Must have
• A both-and feeling to it (see description), e.g., masculine AND feminine, business AND humanness. Power with, not power over...
Should not have
• Too much "bling" - no classic status symbol business success language

```html
<!DOCTYPE html>
<html lang="en">
<head>
<meta charset="utf-8">
<title>ROOTED! The skill and rhythm of guiding teams through calm and delight — Book Cover</title>
<link rel="stylesheet" href="https://fonts.googleapis.com/css2?family=Barlow+Condensed:wght@600&family=Roboto+Condensed:wght@300&display=swap">
<style>
  :root {
    --page-bg: #e8e9eb;
    --yellow-deep: #fcc010;
    --yellow-mid: #f8cf3a;
    --yellow-light: #f8e487;
    --blue: #1c94d2;
    --white: #ffffff;
  }
  * { margin: 0; padding: 0; box-sizing: border-box; }
  html, body {
    width: 1200px;
    height: 849px;
    overflow: hidden;
    background: var(--page-bg);
  }
  .book-cover {
    position: absolute;
    left: 324px;
    top: 34px;
    width: 551px;
    height: 780px;
    background: linear-gradient(215deg, var(--yellow-light) 0%, var(--yellow-mid) 42%, var(--yellow-deep) 78%, var(--yellow-deep) 100%);
    box-shadow: 10px 12px 22px rgba(60, 60, 70, 0.45);
  }
  .book-title {
    position: absolute;
    left: 48px;
    top: 40px;
    font-family: "Barlow Condensed", "Roboto Condensed", sans-serif;
    font-weight: 600;
    font-size: 130px;
    line-height: 112px;
    color: var(--blue);
  }
  .book-title span { display: block; }
  .author-name {
    position: absolute;
    right: 49px;
    top: 68px;
    font-family: "Roboto Condensed", "Barlow Condensed", sans-serif;
    font-weight: 300;
    font-size: 29px;
    line-height: 38px;
    color: var(--white);
    text-align: right;
    text-transform: uppercase;
  }
  .subtitle {
    position: absolute;
    right: 49px;
    top: 398px;
    font-family: "Roboto Condensed", "Barlow Condensed", sans-serif;
    font-weight: 300;
    font-size: 25px;
    line-height: 31px;
    color: var(--white);
    text-align: right;
  }
  .subtitle span { display: block; }
</style>
</head>
<body>
  <main class="book-cover">
    <h1 class="book-title" aria-label="ROOTED!">
      <span>R</span>
      <span>O</span>
      <span>O</span>
      <span>T</span>
      <span>E</span>
      <span>D</span>
    </h1>

    <p class="author-name">Author’s<br>Name</p>

    <p class="subtitle">
      <span>The</span>
      <span>skill</span>
      <span>and</span>
      <span>rhythm</span>
      <span>of</span>
      <span>guiding</span>
      <span>teams</span>
      <span>through</span>
      <span>calm</span>
      <span>and</span>
      <span>delight</span>
    </p>
  </main>
</body>
</html>
```